Label Design for Cook Marsh Kimchi Sauce – Modern Korean Fermentation Brand

We are developing the primary packaging identity for COOK MARSH, beginning with our flagship Korean Kimchi Sauce.
Cook Marsh is a contemporary Korean food brand built around an idea that is central to Korean cuisine: Tradition refined through modern food science. Our kimchi sauce is not intended to be simply another spicy Korean condiment, but rooted in authentic Korean kimchi fermentation and combines traditional fermentation knowledge with modern process control to create a consistent, flavorful and convenient shelf-stable sauce.
The goal of this project is to create a distinctive, typography-led master label and visual identity that can eventually expand across an entire Cook Marsh product family. The winning design should feel credible as the beginning of a serious international food brand, rather than as a one-off sauce label.
This first project is for our Kimchi Sauce bottle and Kimchi Paste package, but the design should establish a master brand system that can later expand into additional products such as Korean Kimchi Sauce and Korean Kimchi Paste.
Primary sauce bottle is approximately:
300 mL / 10.1 FL OZ
The label design should be developed specifically with the proportions, readability and shelf presence of a 300 mL sauce bottle in mind.
We want the design to place much greater emphasis on text, font, typography and brand hierarchy than on graphics or illustration. Should be driven primarily by distinctive typography, strong font selection or custom lettering, clear hierarchy, strong use of scale and proportion, memorable wordmark treatment, spacing and composition, recognizable label structure, with Cook Marsh and Kimchi Sauce as the visual focus. Graphics and illustrations can be used, but they should be secondary and restrained, not the main feature of the package.
A brand such as Verluna, particularly its 300 mL bottle presentation, is useful as a general reference for the importance of typography, simplicity, hierarchy, shelf recognition and longevity. We are not looking to copy Verluna's design, but we appreciate how strongly the brand is communicated through text and label structure rather than decorative graphics.
The brand concept combines:
• Korean fermentation heritage
• modern scientific precision
• real food / plant-forward ingredients
• global culinary versatility
Front Label Priorities
The front label should clearly communicate:
1. COOK MARSH as the master brand
2. KIMCHI SAUCE as the product
3. 300 mL / 10.1 FL OZ
4. A premium, clean and modern aesthetic
5. An appetizing and confident Korean identity
Possible supporting themes or optional secondary messaging:
• Authentically Fermented
• Crafted for Consistency
• Korean Chili Blend
• Bold & Tangy
• Tradition Refined by Science
These are secondary messages only. We prefer strong typography and hierarchy over excessive front-label copy. We are open to creative exploration, but the design should feel typography-led, modern, premium, bold, clean, warm, appetizing, rooted in Korean heritage, recognizable from a distance, scalable across future products
Please keep graphics minimal and secondary.
Ingredient illustrations such as cabbage, chili peppers, garlic or herbs may be used if they support the design, but they should not dominate the label.
Our preliminary concepts use more ingredient illustration than we ultimately want. We are sharing them as a starting point, but we would like designers to move the brand toward a cleaner, stronger and more typography-focused identity.
A strong concept should still work even if most decorative graphics were removed.
Please avoid:
• illustration-heavy labels
• overly busy ingredient graphics
• overly rustic packaging
• typography that feels generic or secondary
• copycat designs of existing trendy sauce brands
The final design should make the consumer remember COOK MARSH, not simply the pictures on the bottle.

```html
<!DOCTYPE html>
<html lang="en">
<head>
<meta charset="utf-8">
<title>Cook Marsh Kimchi Sauce Label</title>
<link rel="stylesheet" href="https://fonts.googleapis.com/css2?family=Anton&family=Archivo+Black&family=Montserrat:wght@500&family=Oswald:wght@500;600&display=swap">
<style>
  :root {
    --paper: #f7f4ea;
    --chili-red: #c62a2d;
    --maroon: #5a1f2c;
    --leaf-green: #4bb54a;
    --page: #ffffff;
  }
  * { margin: 0; padding: 0; box-sizing: border-box; }
  html, body {
    width: 1200px;
    height: 1200px;
    overflow: hidden;
    background: var(--page);
  }
  .canvas {
    position: relative;
    width: 1200px;
    height: 1200px;
  }
  .label {
    position: absolute;
    left: 310px;
    top: 42px;
    width: 580px;
    height: 1116px;
    background: var(--paper);
    border: 2px solid var(--maroon);
    border-radius: 290px 290px 56px 56px / 330px 330px 56px 56px;
  }
  .brand {
    position: absolute;
    left: 0;
    right: 0;
    top: 130px;
    text-align: center;
    font-family: 'Montserrat', sans-serif;
    font-weight: 500;
    color: var(--chili-red);
    line-height: 1;
  }
  .brand-small {
    display: block;
    font-size: 19px;
    letter-spacing: 0.42em;
    padding-left: 0.42em;
  }
  .brand-large {
    display: block;
    margin-top: 10px;
    font-size: 66px;
    letter-spacing: -0.02em;
  }
  .headline {
    position: absolute;
    left: 0;
    top: 0;
    width: 580px;
    height: 1116px;
  }
  .pill-text {
    font-family: 'Oswald', sans-serif;
    font-weight: 600;
    font-size: 28px;
    fill: var(--paper);
  }
  .kimchi {
    font-family: 'Anton', sans-serif;
    font-size: 420px;
  }
  .sauce {
    font-family: 'Archivo Black', sans-serif;
    font-size: 84px;
  }
  .claims {
    position: absolute;
    left: 0;
    right: 0;
    top: 918px;
    text-align: center;
    font-family: 'Oswald', sans-serif;
    font-weight: 500;
    color: var(--maroon);
    font-size: 30px;
    line-height: 48px;
  }
  .volume {
    position: absolute;
    left: 0;
    right: 0;
    top: 1052px;
    text-align: center;
    font-family: 'Oswald', sans-serif;
    font-weight: 500;
    color: var(--maroon);
    font-size: 29px;
  }
</style>
</head>
<body>
<main class="canvas">
  <section class="label">
    <div class="brand">
      <span class="brand-small">COOK</span>
      <span class="brand-large">MARSH</span>
    </div>

    <svg class="headline" viewBox="0 0 580 1116" xmlns="http://www.w3.org/2000/svg" aria-label="Korean Chili Blend Kimchi Sauce">
      <g class="tag" transform="rotate(-3 290 350)">
        <rect x="112" y="330" width="356" height="42" rx="21" fill="var(--leaf-green)"/>
        <text class="pill-text" x="290" y="363" text-anchor="middle" textLength="280" lengthAdjust="spacingAndGlyphs">KOREAN CHILI BLEND</text>
      </g>

      <g class="product-name" transform="rotate(-4 290 560)">
        <text class="kimchi" x="26" y="752" fill="var(--maroon)" textLength="486" lengthAdjust="spacingAndGlyphs">KIMCHI</text>
        <text class="kimchi" x="36" y="742" fill="var(--chili-red)" stroke="var(--maroon)" stroke-width="2" textLength="486" lengthAdjust="spacingAndGlyphs">KIMCHI</text>
      </g>

      <g class="product-type" transform="rotate(-4 290 805)">
        <rect x="114" y="752" width="336" height="118" fill="var(--maroon)"/>
        <rect x="122" y="744" width="336" height="118" fill="var(--leaf-green)" stroke="var(--paper)" stroke-width="4"/>
        <text class="sauce" x="286" y="840" text-anchor="middle" fill="var(--maroon)" textLength="276" lengthAdjust="spacingAndGlyphs">SAUCE</text>
        <text class="sauce" x="290" y="835" text-anchor="middle" fill="var(--paper)" textLength="276" lengthAdjust="spacingAndGlyphs">SAUCE</text>
      </g>
    </svg>

    <p class="claims">BOLD &amp; TANGY<br>AUTHENTICALLY FERMENTED</p>
    <p class="volume">300 ML / 10.1 FL OZ</p>
  </section>
</main>
</body>
</html>
```